Forge Night Club Flyer, need asap for party this weekend

Text is drawn as an attachment

Need a flyer for club night this Saturday. Guaranteed project need quick turnaround. Image attached, and the FORGE logo to be large and detailed like a sign. The dj names KESTREL, MR. HALVORNE, AND DESMOND K. ORLEY can be large too. It's for house/electronic music in a nice classy venue. High Res image attached.

Target Market(s)

21-40 year old house music lovers, club business

Industry/Entity Type

Night Club

Font styles to use
Sans Serif

Colors
ffffff
cadf82
33a6d7
0356a4
fbee3d

Requirements
Must have
• Either the girl in hard hat or tool belt image, or something similar to stick with the Forge theme. Also the dj names needs to be the same size
Nice to have
• Faded image or some lining around the images so it doesn't look like a plain photo. Black and white is good or faded.
Should not have
• Any cursive or anything not professional looking

```html
<!DOCTYPE html>
<html lang="en">
<head>
<meta charset="utf-8">
<title>Forge – House &amp; Tech Workers</title>
<link rel="stylesheet" href="https://fonts.googleapis.com/css2?family=Germania+One&family=Share+Tech+Mono&family=Jura:wght@500;600&family=Tinos&display=swap">
<style>
  :root {
    --page: #2b2d30;
    --ink: #ffffff;
    --sun: #f2d36a;
    --amber: #e79a2a;
    --ember: #c8361f;
    --flag: #e0333a;
    --night: #140806;
    --steel-face: #d9f1f2;
    --steel-edge: #6c7375;
    --steel-dark: #3a3f41;
    --skin: #c98d62;
    --belt: #d89a35;
    --denim: #3f4d6b;
  }
  * { box-sizing: border-box; margin: 0; padding: 0; }
  html, body { width: 1200px; height: 900px; overflow: hidden; background: var(--page); }
  .flyer {
    position: absolute; left: 20px; top: 41px; width: 1160px; height: 818px; overflow: hidden;
    background:
      linear-gradient(180deg, rgba(0,0,0,0) 45%, rgba(20,8,6,.65) 82%, var(--night) 100%),
      linear-gradient(160deg, #f6e7a6 0%, var(--sun) 22%, var(--amber) 45%, var(--ember) 70%, #5a120c 100%);
  }
  .flyer__shards { position: absolute; inset: 0; }
  .flyer__photo {
    position: absolute; left: 0; top: 0; width: 480px; height: 818px;
    background:
      linear-gradient(180deg, #a8393a 0%, #c9a9a2 6%, var(--skin) 14%, #b87b52 50%, var(--belt) 62%, #b97a24 80%, var(--denim) 92%, #2c1d14 100%);
    -webkit-mask-image: linear-gradient(90deg, #000 78%, transparent 100%);
            mask-image: linear-gradient(90deg, #000 78%, transparent 100%);
  }
  .age-note {
    position: absolute; right: 18px; top: 10px;
    font: 400 21px 'Tinos', serif; color: var(--ink);
  }
  .title {
    position: absolute; left: 515px; top: 30px; width: 560px; text-align: center;
    font: 400 200px/1 'Germania One', serif; letter-spacing: 2px; color: var(--steel-face);
    text-shadow: 1px 1px 0 var(--steel-edge), 2px 2px 0 var(--steel-edge), 3px 3px 0 var(--steel-edge),
                 4px 4px 0 var(--steel-dark), 5px 5px 0 var(--steel-dark), 8px 10px 14px rgba(0,0,0,.45);
  }
  .subtitle {
    position: absolute; left: 500px; top: 247px; width: 600px; text-align: center;
    font: 400 42px 'Share Tech Mono', monospace; color: var(--ink); letter-spacing: 1px;
  }
  .lineup {
    position: absolute; left: 482px; top: 352px; width: 600px; text-align: center;
    font: 500 38px/38px 'Jura', sans-serif; color: var(--ink); letter-spacing: 6px; list-style: none;
  }
  .date-band {
    position: absolute; left: 542px; top: 518px; width: 484px; height: 66px;
    display: flex; align-items: center; justify-content: center;
    font: 400 34px 'Share Tech Mono', monospace; color: var(--ink);
  }
  .date-band svg { position: absolute; inset: 0; z-index: 0; }
  .date-band span { position: relative; }
  .venue-mark {
    position: absolute; left: 1040px; top: 540px;
    font: 400 20px 'Share Tech Mono', monospace; color: var(--ink);
  }
  .venue {
    position: absolute; left: 480px; top: 622px; width: 480px; text-align: center;
    font: 400 48px 'Share Tech Mono', monospace; color: var(--ink); letter-spacing: 2px;
  }
  .contact {
    position: absolute; left: 480px; top: 706px; width: 480px; text-align: center;
    font: 400 20px/30px 'Share Tech Mono', monospace; color: var(--ink);
  }
  .contact__address { font-size: 25px; }
</style>
</head>
<body>
  <main class="flyer">
    <svg class="flyer__shards" viewBox="0 0 1160 818" aria-hidden="true">
      <polygon points="880,0 1160,0 1160,120 1010,190" fill="#d9322b" opacity=".9"/>
      <polygon points="640,290 1160,290 900,620" fill="#b02a1e" opacity=".35"/>
      <polygon points="560,300 700,300 630,450" fill="#f5d25a" opacity=".35"/>
      <polygon points="860,560 1160,300 1160,818 960,818" fill="#5a0d0a" opacity=".35"/>
    </svg>
    <div class="flyer__photo" role="img" aria-label="Photo of a woman's midriff in a knotted plaid shirt and denim shorts, wearing a leather tool belt with wrenches, pliers and a hammer"></div>

    <p class="age-note">21+ WELCOME</p>
    <h1 class="title">FORGE</h1>
    <p class="subtitle">HOUSE &amp; TECH WORKERS</p>
    <ul class="lineup">
      <li>KESTREL</li>
      <li>MR. HALVORNE</li>
      <li>DESMOND K. ORLEY</li>
    </ul>
    <div class="date-band">
      <svg viewBox="0 0 484 66" preserveAspectRatio="none" aria-hidden="true"><polygon points="28,0 484,0 456,66 0,66" fill="var(--flag)"/></svg>
      <span>SAT 3/12/16 10p-2a</span>
    </div>
    <p class="venue-mark">ORRIN</p>
    <p class="venue">ORRIN LOUNGE</p>
    <p class="contact">
      FOR RESERVATIONS CALL 555-014-2280<br>
      <span class="contact__address">742 W. Harbor Ave, Fairmont, CA</span>
    </p>
  </main>
</body>
</html>
```